A4 Single Page Brochure for Private Cloud Offerings

Theme: Futuristic Tech Company

Brightmoor Systems is looking to offer private cloud services for our enterprise customers in Perth-based data-centres that provides our clients with a lower-cost alternative to Nimbra or KLT yielding better performance.

We are looking for a single A4 brochure with a great graphics design theme to promote these services.

We will be providing five tiers:
- Starter
- Growth
- Professional
- Premier
- Elite

Each plan must list on the brochure the Max VMs, CPU cores, Memory and SSD storage allocated. Refer to the uploaded PNG file.

The brochure must list the following selling points:

- Hosted in a local Perth-based TIER3 and TIER4 datacentres
- WA owned hosting - support local
- Low latency - ultra fast local hosting
- Includes Quorra Host Datacentre licensing
- Includes WallHaven Managed Firewalls for Enterprise level threat detection
- Includes all infrastructure maintenance services
- Full self management of VMs through customer portal
- Includes a 1gbps Internet link
- Predictable fixed monthly fee with no dynamic billing
- No additional charges for Storage Transactions, Internet Usage, VM Snapshots, Datacentre Bandwidth Usage and Firewall Traffic Usage.
- Highly available cluster, no single point of failure.
- Pricing is based on 36 months commit
- Yearly rate increases capped to a maximum of Australian CPI
- All plans have 24/7/365 support with dedicated after hours number.
- Managed backup and managed disaster recovery services can be added to plans

Service provided in accordance with our terms and conditions.

We need the ability to EDIT the brochure to adjust pricing after we receive the final project.

Please do not utilise "Pushing the Boundaries of Technology" - our brand is being replaced with "Specialised Consulting". New website is under development but not launched yet.

Target Market(s)

Information Technology Sector

Colors
0054AA
0677BA
7BADD7
CADEEF
E8F1F8

Requirements
Must have
• Theme of Brightmoor is Blue
Should not have
• Extremely stock imagary that just looks "cheap and stock"

```html
<!DOCTYPE html>
<html lang="en">
<head>
<meta charset="utf-8">
<title>Brightmoor Systems – Private Cloud Services</title>
<link href="https://fonts.googleapis.com/css2?family=Orbitron:wght@700;800&family=Montserrat:wght@700;800&family=Poppins:wght@300;400;500;600;700&display=swap" rel="stylesheet">
<style>
  :root{
    --navy:#0b1463;
    --navy-deep:#08104f;
    --blue:#0054AA;
    --blue-mid:#0677BA;
    --blue-bright:#1f8ff0;
    --blue-soft:#7BADD7;
    --blue-pale:#CADEEF;
    --blue-mist:#E8F1F8;
    --grey-bar:#c9c9cc;
    --ink:#1d1d24;
    --white:#ffffff;
  }
  *{box-sizing:border-box;margin:0;padding:0}
  html,body{width:908px;height:1200px;overflow:hidden;background:var(--white)}
  body{font-family:"Poppins",sans-serif;color:var(--ink)}
  .brochure{position:relative;width:908px;height:1200px;overflow:hidden;background:var(--white)}
  .abs{position:absolute}

  .brand{left:52px;top:86px;display:flex;align-items:center;gap:10px;
    font-family:"Poppins",sans-serif;font-weight:700;font-size:27px;color:var(--navy);letter-spacing:.5px}
  .brand-mark{width:14px;height:14px;background:var(--navy)}

  .hero-shapes{left:0;top:0;width:908px;height:560px}

  .hero-title{left:49px;top:196px;font-family:"Orbitron",sans-serif;font-weight:800;
    font-size:44px;line-height:45px;color:var(--white);letter-spacing:.5px}
  .hero-title .accent{color:var(--blue-bright)}
  .hero-sub{left:49px;top:345px;padding-left:14px;border-left:3px solid var(--blue-bright);
    color:var(--white);font-weight:600;font-size:16.5px;line-height:21px}

  .intro{left:452px;top:405px;width:440px;color:var(--white);font-size:16.6px;line-height:20.6px;font-weight:400}

  .tiers-heading{left:52px;top:566px;font-weight:300;font-size:18.5px;line-height:20px;color:var(--navy)}

  .tier-head{top:571px;width:112px;height:27px;border-radius:4px;color:var(--white);
    font-weight:700;font-size:11px;display:flex;align-items:center;justify-content:center;letter-spacing:.2px}
  .col{top:606px;width:112px;height:151px;border-radius:0 0 10px 10px}
  .col.blueish{background:linear-gradient(180deg,#fff 0%,#dbe6f1 30%,#aac5df 55%,#8fb2d6 100%)}
  .col.greyish{background:linear-gradient(180deg,#fff 0%,#e2e2e4 30%,#cfcfd2 55%,#bcbcc0 100%)}
  .cell{width:112px;height:26px;display:flex;align-items:center;justify-content:center;
    font-weight:600;font-size:13.5px;color:var(--ink)}
  .row-label{left:52px;width:360px;height:26px;display:flex;align-items:center;padding-left:14px;
    font-family:"Montserrat",sans-serif;font-weight:800;font-size:13px;letter-spacing:3px;color:var(--white);border-radius:5px 0 0 5px}
  .cost{top:765px;width:112px;height:26px;border-radius:5px;background:var(--navy);color:var(--white);
    display:flex;align-items:center;justify-content:center;font-weight:700;font-size:13px}

  .offer-title{left:52px;top:806px;font-family:"Montserrat",sans-serif;font-size:23px;letter-spacing:3.5px;color:var(--navy);font-weight:800}
  .offer-title span{color:var(--blue);font-family:"Poppins",sans-serif;font-weight:300;letter-spacing:4px}
  .offer-frame{left:0;top:0;width:908px;height:1200px;pointer-events:none}
  .divider{top:858px;width:1px;height:210px;background:#d8d8dc}

  .offer-list{list-style:none;font-size:11.3px;line-height:13.8px;color:#222}
  .offer-list li{position:absolute;left:0;white-space:nowrap}
  .tick{position:absolute;width:9px;height:9px}

  .terms{left:0;width:908px;top:1096px;text-align:center;font-family:"Montserrat",sans-serif;font-weight:700;font-size:8.5px;letter-spacing:4.2px;color:var(--navy)}

  .contact{top:1130px;font-size:16px;color:var(--ink);display:flex;align-items:center;gap:4px;white-space:nowrap}
  .call{font-family:"Orbitron",sans-serif;font-weight:700;font-size:14.5px}
  .call span{color:var(--blue)}
  .web{font-weight:600}
  .icon{width:12px;height:12px}
</style>
</head>
<body>
<main class="brochure">

  <svg class="abs hero-shapes" viewBox="0 0 908 560" aria-hidden="true">
    <defs>
      <linearGradient id="bandFill" x1="0" y1="0" x2="1" y2="1">
        <stop offset="0" stop-color="#0c1f86"/>
        <stop offset="1" stop-color="#07105a"/>
      </linearGradient>
      <linearGradient id="frameFill" x1="0" y1="0" x2="1" y2="1">
        <stop offset="0" stop-color="#1b2aa8"/>
        <stop offset="1" stop-color="#0b1463"/>
      </linearGradient>
    </defs>
    <polygon points="0,165 519,165 400,421 0,421" fill="url(#bandFill)"/>
    <polygon points="693,1 470,354 908,387 908,150" fill="url(#frameFill)"/>
    <polygon points="456,388 478,367 568,367 546,388" fill="var(--grey-bar)"/>
    <polygon points="578,388 600,367 827,367 849,388" fill="var(--grey-bar)"/>
    <polygon points="434,396 908,396 908,553 348,553" fill="var(--blue)"/>
  </svg>

  <svg class="abs" style="left:519px;top:54px" width="364" height="310" viewBox="0 0 364 310" role="img" aria-label="Photo of an open laptop on a desk, screen showing a cloud network diagram">
    <defs>
      <linearGradient id="photoFill" x1="0" y1="0" x2="1" y2="1">
        <stop offset="0" stop-color="#dfe7f0"/>
        <stop offset=".55" stop-color="#9aa3ad"/>
        <stop offset="1" stop-color="#a57d55"/>
      </linearGradient>
    </defs>
    <polygon points="175,0 0,310 364,310" fill="url(#photoFill)"/>
  </svg>

  <div class="abs brand"><span class="brand-mark"></span>Brightmoor Systems</div>

  <h1 class="abs hero-title"><span class="accent">PRIVATE</span><br>CLOUD<br>SERVICES</h1>
  <p class="abs hero-sub">For our enterprise customers in<br>Perth-based data-centres</p>

  <p class="abs intro">Brightmoor Systems is looking to offer private cloud services for our enterprise customers in Perth-based data-centres that provides our clients with a lower-cost alternative to Nimbra or KLT yielding better performance.</p>

  <h2 class="abs tiers-heading">WE WILL BE<br>PROVIDING FIVE TIERS</h2>

  <div class="abs tier-head" style="left:283px;background:var(--navy)">STARTER</div>
  <div class="abs tier-head" style="left:399px;background:var(--blue)">GROWTH</div>
  <div class="abs tier-head" style="left:514px;background:var(--navy)">PROFESSIONAL</div>
  <div class="abs tier-head" style="left:629px;background:var(--blue)">PREMIER</div>
  <div class="abs tier-head" style="left:745px;background:var(--navy)">ELITE</div>

  <div class="abs row-label" style="top:613px;background:var(--navy)">MAX VMS</div>
  <div class="abs row-label" style="top:652px;background:var(--blue)">CPU CORES</div>
  <div class="abs row-label" style="top:691px;background:var(--navy)">MEMORY</div>
  <div class="abs row-label" style="top:731px;background:var(--blue)">SSD STORAGE</div>

  <div class="abs col blueish" style="left:283px"></div>
  <div class="abs col greyish" style="left:399px"></div>
  <div class="abs col blueish" style="left:514px"></div>
  <div class="abs col greyish" style="left:629px"></div>
  <div class="abs col blueish" style="left:745px"></div>

  <div class="abs" style="left:283px;top:613px">
    <div class="cell">5</div><div class="cell" style="margin-top:13px">8</div><div class="cell" style="margin-top:13px">64</div><div class="cell" style="margin-top:14px">3</div>
  </div>
  <div class="abs" style="left:399px;top:613px">
    <div class="cell">10</div><div class="cell" style="margin-top:13px">16</div><div class="cell" style="margin-top:13px">128</div><div class="cell" style="margin-top:14px">8</div>
  </div>
  <div class="abs" style="left:514px;top:613px">
    <div class="cell">15</div><div class="cell" style="margin-top:13px">32</div><div class="cell" style="margin-top:13px">192</div><div class="cell" style="margin-top:14px">15</div>
  </div>
  <div class="abs" style="left:629px;top:613px">
    <div class="cell">20</div><div class="cell" style="margin-top:13px">48</div><div class="cell" style="margin-top:13px">256</div><div class="cell" style="margin-top:14px">20</div>
  </div>
  <div class="abs" style="left:745px;top:613px">
    <div class="cell">25</div><div class="cell" style="margin-top:13px">64</div><div class="cell" style="margin-top:13px">320</div><div class="cell" style="margin-top:14px">30</div>
  </div>

  <div class="abs row-label" style="top:765px;width:227px;background:var(--blue);border-radius:5px">MONTHLY COST</div>
  <div class="abs cost" style="left:283px">$1,028.01</div>
  <div class="abs cost" style="left:399px">$3,426.64</div>
  <div class="abs cost" style="left:514px">$4,626.05</div>
  <div class="abs cost" style="left:629px">$5,482.72</div>
  <div class="abs cost" style="left:745px">$7,196.07</div>

  <h2 class="abs offer-title">WHAT <span>WE OFFER</span></h2>
  <svg class="abs offer-frame" viewBox="0 0 908 1200" aria-hidden="true">
    <path d="M350 823 H853 Q865 823 865 835 V1078 Q865 1090 853 1090 H64 Q52 1090 52 1078 V1071" fill="none" stroke="var(--blue)" stroke-width="1.2"/>
    <circle cx="52" cy="1071" r="2.6" fill="var(--blue)"/>
  </svg>
  <div class="abs divider" style="left:281px"></div>
  <div class="abs divider" style="left:569px"></div>

  <svg width="0" height="0" style="position:absolute">
    <symbol id="tick" viewBox="0 0 10 10">
      <circle cx="5" cy="5" r="5" fill="#3d8fe0"/>
      <path d="M2.8 5.2 L4.4 6.7 L7.3 3.6" fill="none" stroke="#fff" stroke-width="1.3" stroke-linecap="round"/>
    </symbol>
  </svg>

  <ul class="abs offer-list" style="left:80px;top:854px">
    <li style="top:0">Hosted in a local<br>Perth-based TIER3 and<br>TIER4 datacentres</li>
    <li style="top:55px">WA owned hosting -<br>support local</li>
    <li style="top:96px">Low latency-<br>ultra fast local hosting</li>
    <li style="top:137px">Includes Quorra Host<br>Datacentre licensing</li>
    <li style="top:178px">Includes WallHaven Managed<br>Firewalls for Enterprise level<br>threat detection</li>
  </ul>
  <ul class="abs offer-list" style="left:328px;top:854px">
    <li style="top:0">Includes all infrastructure<br>maintenance services</li>
    <li style="top:41px">Full self management<br>of VMs through customer portal</li>
    <li style="top:82px">Includes a 1gbps<br>Internet link</li>
    <li style="top:123px">Predictable fixed monthly<br>fee with no dynamic billing</li>
    <li style="top:164px">No additional charges for Storage<br>Transactions, Internet Usage, VM<br>Snapshots, Datacentre Bandwidth<br>Usage and Firewall Traffic Usage.</li>
  </ul>
  <ul class="abs offer-list" style="left:622px;top:854px">
    <li style="top:0">Highly available cluster, no<br>single point of failure.</li>
    <li style="top:41px">Pricing is based on 36<br>months commit</li>
    <li style="top:82px">Yearly rate increases capped to a<br>maximum of Australian CPI</li>
    <li style="top:123px">All plans have 24/7/365 support with<br>dedicated after hours number.</li>
    <li style="top:164px">Managed backup and managed<br>disaster recovery services can be<br>added to plans</li>
  </ul>

  <svg class="abs tick" style="left:60px;top:856px"><use href="#tick"/></svg>
  <svg class="abs tick" style="left:60px;top:911px"><use href="#tick"/></svg>
  <svg class="abs tick" style="left:60px;top:952px"><use href="#tick"/></svg>
  <svg class="abs tick" style="left:60px;top:993px"><use href="#tick"/></svg>
  <svg class="abs tick" style="left:60px;top:1034px"><use href="#tick"/></svg>
  <svg class="abs tick" style="left:309px;top:856px"><use href="#tick"/></svg>
  <svg class="abs tick" style="left:309px;top:897px"><use href="#tick"/></svg>
  <svg class="abs tick" style="left:309px;top:938px"><use href="#tick"/></svg>
  <svg class="abs tick" style="left:309px;top:979px"><use href="#tick"/></svg>
  <svg class="abs tick" style="left:309px;top:1020px"><use href="#tick"/></svg>
  <svg class="abs tick" style="left:602px;top:856px"><use href="#tick"/></svg>
  <svg class="abs tick" style="left:602px;top:897px"><use href="#tick"/></svg>
  <svg class="abs tick" style="left:602px;top:938px"><use href="#tick"/></svg>
  <svg class="abs tick" style="left:602px;top:979px"><use href="#tick"/></svg>
  <svg class="abs tick" style="left:602px;top:1020px"><use href="#tick"/></svg>

  <p class="abs terms">SERVICE PROVIDED IN ACCORDANCE WITH OUR TERMS AND CONDITIONS</p>

  <div class="abs contact call" style="left:52px">Call Us&nbsp;<span>Now!</span></div>
  <div class="abs contact" style="left:262px">
    <svg class="icon" viewBox="0 0 12 12" aria-hidden="true"><circle cx="6" cy="6" r="6" fill="var(--blue)"/><path d="M4 3 Q3.3 3.4 3.6 4.6 Q4.5 7.2 7.3 8.4 Q8.5 8.7 8.9 8 L7.9 7.1 L7.1 7.6 Q5.5 6.8 4.9 5.1 L5.4 4.3 Z" fill="#fff"/></svg>
    618 5530 2194
  </div>
  <div class="abs contact" style="left:396px">
    <svg class="icon" viewBox="0 0 12 12" aria-hidden="true"><circle cx="6" cy="6" r="6" fill="var(--blue)"/><rect x="3" y="4" width="6" height="4.2" fill="none" stroke="#fff" stroke-width=".9"/><path d="M3 4 L6 6.4 L9 4" fill="none" stroke="#fff" stroke-width=".9"/></svg>
    info@brightmoor.com
  </div>
  <div class="abs contact web" style="left:592px">
    <svg class="icon" viewBox="0 0 12 12" aria-hidden="true"><circle cx="6" cy="6" r="6" fill="var(--blue)"/><circle cx="6" cy="6" r="3.3" fill="none" stroke="#fff" stroke-width=".8"/><ellipse cx="6" cy="6" rx="1.4" ry="3.3" fill="none" stroke="#fff" stroke-width=".8"/><path d="M2.7 6 H9.3" stroke="#fff" stroke-width=".8"/></svg>
    www.brightmoor.com
  </div>

</main>
</body>
</html>
```